【 概要 】 新発売するまつげ美容液のパッケージ、ロゴデザインを募集します。 【 依頼内容 】 ●容器、化粧箱それぞれに印刷する商品名ロゴ&デザイン ●成分・製造元・JANなどを入れるスペースがあるため、基本的に片面に収まる範囲でお願いします(資料参考) ・商品名「Korunela Eyelash Serum」 ・ロゴブランド名「Korunela」 ・ 容器のフォントは4.5pt以上 ・色は黒一色 ・縦・横どちらでもOK 【 デザインイメージ 】 ・ターゲット層:20〜40代男女 ・雰囲気:初めての人や男性でも選びやすい ・シンプルだけどおしゃれなデザインにしたい ・ロゴメインでも、商品名メインでもOKですが、両方入れてほしい 【 契約金額(税抜) 】 2万円 ※契約金額(税込)からシステム利用料を差し引いた金額が、ワーカーさまの受取金額となります その他ご質問等ありましたら、気軽にお問い合わせください。 ご応募をお待ちしております! |
採用の理由
どの案も特徴があり、シンプルながらおしゃれなデザインのものばかりでとても悩みましたが、
ロゴデザインが気に入りましたので、こちらのデザインを採用させて頂きます。
応募者全員へのお礼・コメント
皆様お忙しい中、ご提案いただきましてありがとうございました。
また新商品を出す際には宜しくお願いいたします。

```html
<!DOCTYPE html>
<html lang="en">
<head>
<meta charset="utf-8">
<title>Korunela Eyelash Serum – Packaging</title>
<link href="https://fonts.googleapis.com/css2?family=Kaushan+Script&display=swap" rel="stylesheet">
<style>
  :root {
    --ink: #111111;
    --paper: #ffffff;
    --cut: #555555;
    --fold: #e0574a;
  }
  html, body { margin: 0; padding: 0; overflow: hidden; background: var(--paper); }
  .artboard { display: block; width: 1200px; height: 832px; }
  .cut-line { fill: none; stroke: var(--cut); stroke-width: 0.6; }
  .fold-line { fill: none; stroke: var(--fold); stroke-width: 0.6; stroke-dasharray: 2 1.5; }
  .brand-text, .product-name, .bottle-text {
    font-family: "Kaushan Script", "Brush Script MT", cursive;
    font-weight: 400;
  }
  .brand-text { fill: var(--ink); }
  .product-name { fill: var(--ink); font-size: 16px; }
  .bottle-text { font-size: 9px; }
  .ink-fill { fill: var(--ink); }
  .paper-fill { fill: var(--paper); }
  .bottle-outline { fill: var(--paper); stroke: var(--ink); stroke-width: 0.7; }
  .bottle-dark { fill: var(--ink); stroke: var(--ink); stroke-width: 0.7; }
  .thread { stroke: var(--ink); stroke-width: 0.6; fill: none; }
</style>
</head>
<body>
<svg class="artboard" viewBox="0 0 600 416" xmlns="http://www.w3.org/2000/svg">

  <g class="carton">
    <path class="cut-line" d="
      M88 185 L88 150 L105 150 L105 114 Q105 108 111 108 L314 108 Q320 108 320 114 L320 150 L333 150 L333 185
      L333 250 L360 252 Q366 253 366 260 L366 290 L333 292
      L370 292 L370 298 L404 298 Q410 298 410 306 L410 376 Q410 384 404 384 L370 384 L370 392 L333 392
      L88 392 L45 392 L45 384 L11 384 Q5 384 5 376 L5 306 Q5 298 11 298 L45 298 L45 292 L88 292
      L55 290 L55 260 Q55 253 61 252 L88 250 Z" />
    <line class="fold-line" x1="105" y1="148" x2="320" y2="148"/>
    <line class="fold-line" x1="88" y1="185" x2="333" y2="185"/>
    <line class="fold-line" x1="88" y1="250" x2="333" y2="250"/>
    <line class="fold-line" x1="88" y1="292" x2="333" y2="292"/>
    <line class="fold-line" x1="88" y1="250" x2="88" y2="392"/>
    <line class="fold-line" x1="333" y1="250" x2="333" y2="392"/>
    <line class="fold-line" x1="45" y1="298" x2="45" y2="384"/>
    <line class="fold-line" x1="370" y1="298" x2="370" y2="384"/>

    <circle class="ink-fill" cx="64" cy="325" r="12"/>

    <g class="front-lockup">
      <circle class="ink-fill" cx="187" cy="306" r="4.5"/>
      <text class="brand-text" x="194" y="309.5" font-size="9.5">Korunela</text>
    </g>
    <text class="product-name" x="210" y="330" text-anchor="middle" textLength="228" lengthAdjust="spacing">Korunela Eyelash Serum</text>
  </g>

  <g class="mark-primary">
    <circle class="ink-fill" cx="470" cy="62" r="30"/>
    <text class="brand-text" x="506" y="69" font-size="18">Korunela</text>
  </g>
  <g class="mark-horizontal">
    <circle class="ink-fill" cx="416" cy="155" r="14"/>
    <text class="brand-text" x="436" y="163" font-size="22">Korunela</text>
  </g>

  <g class="bottle bottle-light">
    <rect class="bottle-outline" x="463" y="228" width="26" height="17" rx="2"/>
    <line class="thread" x1="463" y1="232" x2="489" y2="234"/>
    <line class="thread" x1="463" y1="236" x2="489" y2="238"/>
    <line class="thread" x1="463" y1="240" x2="489" y2="242"/>
    <rect class="bottle-outline" x="457" y="245" width="38" height="150" rx="3"/>
    <circle class="ink-fill" cx="476" cy="270" r="6"/>
    <text class="bottle-text ink-fill" transform="translate(473 282) rotate(90)" textLength="106" lengthAdjust="spacing">Korunela Eyelash Serum</text>
  </g>

  <g class="bottle bottle-dark-version">
    <rect class="bottle-outline" x="523" y="228" width="26" height="17" rx="2"/>
    <line class="thread" x1="523" y1="232" x2="549" y2="234"/>
    <line class="thread" x1="523" y1="236" x2="549" y2="238"/>
    <line class="thread" x1="523" y1="240" x2="549" y2="242"/>
    <rect class="bottle-outline" x="517" y="245" width="38" height="150" rx="3"/>
    <rect class="bottle-dark" x="521" y="252" width="30" height="138" rx="2"/>
    <circle class="paper-fill" cx="536" cy="270" r="6"/>
    <text class="bottle-text paper-fill" transform="translate(533 282) rotate(90)" textLength="106" lengthAdjust="spacing">Korunela Eyelash Serum</text>
  </g>
</svg>
</body>
</html>
```